Landscape Company in need of logo and business card update. Current logo file is attached.

I need a business card design for a Woman Owned Landscape business in Kansas City. I do Native plant installation and maintenance as well as mowing, chemical applications and residential and commercial landscaping.
My colors are navy, green and white.
I currently have a logo that can be used or you can redesign it.

Target Market(s)

Residential and commercial

Industry/Entity Type

Landscape

Contact Information for Business Card

On back of current card it lists what I do and website:
BMP/Raingarden Maintenance and Installation, Certified Chemical Applicator for Trees, shrubs, and turf; Landscape Design and Installation for residential and commercial.

Logo Text

Birchwell Landscape Partners, LLC

Font styles to use
Other font styles liked:
• See current font on logo examples

Requirements
Must have
• Phone number: 913-555-0182
• Website: www.birchwellyards.example
• Colors: Navy, Green, white
• Email: birchwellyards@mailbox.example
• Address: PO BOX 417208 Larkmoor, KS 66990
• Name of Person: Marlene Kozik, owner

```html
<!DOCTYPE html>
<html lang="en">
<head>
<meta charset="utf-8">
<title>Birchwell Landscape – Identity and Business Card</title>
<link href="https://fonts.googleapis.com/css2?family=Arimo:wght@400;700&display=swap" rel="stylesheet">
<style>
  :root {
    --charcoal: #353535;
    --green: #6cbf4a;
    --green-light: #8fd06c;
    --silver: #c2c2c2;
    --silver-dark: #bdbdbd;
    --text-light: #e4e4e4;
    --white: #ffffff;
    --stage: #a65a3a;
  }
  * { box-sizing: border-box; margin: 0; padding: 0; }
  html, body { width: 1098px; height: 1200px; overflow: hidden; }
  body {
    position: relative;
    background: var(--stage);
    font-family: "Arimo", Arial, sans-serif;
  }

  /* Logo panels */
  .logo-panel {
    position: absolute; top: 0; width: 549px; height: 284px;
    display: flex; align-items: center; justify-content: center;
  }
  .logo-panel--dark { left: 0; background: var(--charcoal); }
  .logo-panel--light { left: 549px; background: var(--white); }

  /* Brand lockup */
  .brand { display: flex; flex-direction: column; align-items: center; font-weight: 700; }
  .brand__row { display: flex; align-items: center; gap: 12px; }
  .brand__dot { border-radius: 50%; background: var(--green); }
  .brand__name { color: var(--green); line-height: 1; letter-spacing: 1px; }
  .brand__sub { color: var(--silver); line-height: 1; }
  .logo-panel--light .brand__sub { color: var(--silver-dark); }

  .brand--xl { margin-top: 26px; }
  .brand--xl .brand__dot { width: 36px; height: 36px; }
  .brand--xl .brand__name { font-size: 80px; }
  .brand--xl .brand__sub { font-size: 22px; letter-spacing: 31px; margin-top: 34px; margin-right: -31px; }

  .brand--md .brand__dot { width: 24px; height: 24px; }
  .brand--md .brand__name { font-size: 48px; }
  .brand--md .brand__sub { font-size: 15px; letter-spacing: 20px; margin-right: -20px; }

  /* Cards */
  .card {
    position: absolute; left: 242px; width: 610px; height: 364px;
    background: var(--charcoal); border-radius: 22px; overflow: hidden;
    box-shadow: 0 6px 18px rgba(0,0,0,.35);
  }
  .card--front { top: 354px; }
  .card--back { top: 773px; }

  /* Front */
  .owner { position: absolute; left: 31px; top: 88px; }
  .owner__name { color: var(--green); font-size: 22px; font-weight: 700; }
  .owner__role { color: var(--silver); font-size: 15px; font-weight: 700; margin-top: 4px; }
  .card--front .brand { position: absolute; right: 30px; top: 128px; }
  .card--front .brand__sub { margin-top: 22px; }
  .contact { position: absolute; left: 31px; top: 188px; color: var(--text-light); font-size: 15.5px; list-style: none; }
  .contact__item { display: flex; gap: 7px; align-items: flex-start; line-height: 21px; }
  .contact__item--phone { margin-top: 17px; }
  .contact__item--email { margin-top: 5px; }
  .contact__icon { width: 13px; height: 13px; margin-top: 4px; flex: none; }
  .card__wave { position: absolute; left: 0; bottom: 0; width: 610px; height: 66px; }
  .card__url--front { position: absolute; right: 30px; bottom: 24px; color: var(--white); font-size: 15px; }

  /* Back */
  .card--back .brand { position: absolute; left: 0; right: 0; top: 77px; }
  .card--back .brand__sub { margin-top: 33px; }
  .services {
    position: absolute; left: 0; right: 0; top: 212px;
    text-align: center; color: var(--green); font-size: 15.5px; line-height: 23px;
  }
  .card__url--back {
    position: absolute; left: 0; right: 0; top: 320px;
    text-align: center; color: var(--text-light); font-size: 15.5px; letter-spacing: 1.2px;
  }
</style>
</head>
<body>
  <section class="logo-panel logo-panel--dark">
    <div class="brand brand--xl">
      <div class="brand__row"><span class="brand__dot"></span><span class="brand__name">Birchwell</span></div>
      <span class="brand__sub">LANDSCAPE</span>
    </div>
  </section>
  <section class="logo-panel logo-panel--light">
    <div class="brand brand--xl">
      <div class="brand__row"><span class="brand__dot"></span><span class="brand__name">Birchwell</span></div>
      <span class="brand__sub">LANDSCAPE</span>
    </div>
  </section>

  <article class="card card--front">
    <div class="owner">
      <p class="owner__name">Marlene Kozik</p>
      <p class="owner__role">Owner</p>
    </div>
    <div class="brand brand--md">
      <div class="brand__row"><span class="brand__dot"></span><span class="brand__name">Birchwell</span></div>
      <span class="brand__sub">LANDSCAPE</span>
    </div>
    <ul class="contact">
      <li class="contact__item">
        <svg class="contact__icon" viewBox="0 0 12 12"><path d="M6 0.5a4 4 0 0 1 4 4c0 3-4 7-4 7s-4-4-4-7a4 4 0 0 1 4-4z" fill="none" stroke="#6cbf4a" stroke-width="1.4"/><circle cx="6" cy="4.5" r="1.4" fill="#6cbf4a"/></svg>
        <span>PO BOX 417208 Larkmoor,<br>KS 66990</span>
      </li>
      <li class="contact__item contact__item--phone">
        <svg class="contact__icon" viewBox="0 0 12 12"><path d="M1 4c0-2 10-2 10 0v1H8.5V4h-5v1H1z" fill="#6cbf4a"/><rect x="2" y="6" width="8" height="5" rx="1" fill="#6cbf4a"/><circle cx="6" cy="8.5" r="1.3" fill="#353535"/></svg>
        <span>913-555-0182</span>
      </li>
      <li class="contact__item contact__item--email">
        <svg class="contact__icon" viewBox="0 0 12 12"><rect x="0.5" y="2.5" width="11" height="7.5" fill="#6cbf4a"/><path d="M0.5 2.5 6 7l5.5-4.5" fill="none" stroke="#353535" stroke-width="1"/></svg>
        <span>birchwellyards@mailbox.example</span>
      </li>
    </ul>
    <svg class="card__wave" viewBox="0 0 610 66" preserveAspectRatio="none">
      <path d="M0 6 C120 12 240 26 340 30 C230 30 110 24 0 18 Z" fill="#c2c2c2"/>
      <path d="M0 22 C150 40 330 28 610 4 L610 66 L0 66 Z" fill="#6cbf4a"/>
      <path d="M330 28 C430 16 520 8 610 2 L610 10 C520 14 430 20 330 28 Z" fill="#8fd06c"/>
    </svg>
    <p class="card__url card__url--front">www.birchwellyards.example</p>
  </article>

  <article class="card card--back">
    <div class="brand brand--md">
      <div class="brand__row"><span class="brand__dot"></span><span class="brand__name">Birchwell</span></div>
      <span class="brand__sub">LANDSCAPE</span>
    </div>
    <p class="services">BMP/Raingarden Maintenance and Installation, Certified Chemical<br>Applicator for Trees, shrubs, and turf; Landscape Design and Installation<br>for residential and commercial.</p>
    <p class="card__url card__url--back">www.birchwellyards.example</p>
  </article>
</body>
</html>
```